Welding company needs a business card

We are looking for a logo and business card.

Contact Information for Business Card

418 Bramblecrest Lane
Millbrook, PA 17399
410-555-0173
Kvmetalcraft@forgepostbox.net

```html
<!DOCTYPE html>
<html lang="en">
<head>
<meta charset="utf-8">
<title>KV Metalcraft Inc — Business Card</title>
<link href="https://fonts.googleapis.com/css2?family=Lato:wght@400;700;900&display=swap" rel="stylesheet">
<style>
  :root {
    --stage: #1c1c1c;
    --card-dark: #0d0d0d;
    --card-light: #ffffff;
    --mark-on-dark: #b9b9b9;
    --mark-on-light: #5a5a5a;
    --ink-strong: #3a3a3a;
    --ink-soft: #7a7a7a;
    --rule: #d9d9d9;
  }
  * { box-sizing: border-box; margin: 0; padding: 0; }
  html, body { width: 1200px; height: 900px; overflow: hidden; }
  body {
    background: var(--stage);
    font-family: "Lato", Arial, sans-serif;
    position: relative;
  }
  .card {
    position: absolute;
    left: 320px;
    width: 560px;
    height: 320px;
    border-radius: 24px;
    overflow: hidden;
  }
  .card--back {
    top: 110px;
    background: var(--card-dark);
    display: flex;
    align-items: center;
    justify-content: center;
  }
  .card--front {
    top: 470px;
    background: var(--card-light);
    display: flex;
    align-items: center;
  }
  .brand-name {
    font-weight: 900;
    font-size: 34px;
    letter-spacing: 1px;
    text-transform: uppercase;
    line-height: 1.1;
  }
  .card--back .brand-name { color: var(--mark-on-dark); }
  .card--front .brand {
    width: 270px;
    padding-left: 40px;
  }
  .card--front .brand-name { color: var(--mark-on-light); font-size: 30px; }
  .divider {
    width: 1px;
    height: 190px;
    background: var(--rule);
  }
  .contact {
    padding-left: 28px;
    color: var(--ink-soft);
    font-size: 15px;
    line-height: 1.3;
  }
  .contact .person {
    font-weight: 700;
    font-size: 17px;
    color: var(--ink-strong);
    letter-spacing: 0.5px;
  }
  .contact .role { margin-bottom: 16px; }
  .contact .address { margin-bottom: 12px; }
  .contact .line { display: flex; align-items: center; gap: 7px; }
  .contact svg { width: 13px; height: 13px; fill: var(--ink-strong); flex: none; }
</style>
</head>
<body>
  <section class="card card--back">
    <div class="brand-name">KV Metalcraft Inc</div>
  </section>

  <section class="card card--front">
    <div class="brand">
      <div class="brand-name">KV Metalcraft<br>Inc</div>
    </div>
    <div class="divider"></div>
    <div class="contact">
      <div class="person">MARCUS DELANE</div>
      <div class="role">Managing Director</div>
      <div class="address">418 Bramblecrest Lane<br>Millbrook, PA 17399</div>
      <div class="line">
        <svg viewBox="0 0 16 16" aria-hidden="true"><path d="M3 1h3l1.5 4-2 1.2a9 9 0 0 0 4.3 4.3L11 8.5l4 1.5v3a2 2 0 0 1-2 2A12 12 0 0 1 1 3a2 2 0 0 1 2-2z"/></svg>
        410-555-0173
      </div>
      <div class="line">
        <svg viewBox="0 0 16 16" aria-hidden="true"><path d="M1 3h14v10H1z M2 4l6 5 6-5" fill="none" stroke="#3a3a3a" stroke-width="1.5"/></svg>
        Kvmetalcraft@forgepostbox.net
      </div>
    </div>
  </section>
</body>
</html>
```